Lotus Leaf Kitchen Road Billboard

Road Billboard I need all of this information on it
Authentic Thai Food Bangkok Style
6.5 Miles on the right
4126 Maple Ridge Rd Otto NC
828-555-4172

```html
<!DOCTYPE html>
<html lang="en">
<head>
<meta charset="utf-8">
<title>Lotus Leaf Kitchen Road Billboard</title>
<link href="https://fonts.googleapis.com/css2?family=Poppins:wght@300;400;500;700;800&family=Great+Vibes&display=swap" rel="stylesheet">
<style>
  :root {
    --canvas: #f1f1f1;
    --board: #050505;
    --gold: #d9a522;
    --white: #ffffff;
    --ink: #1c1c1c;
    --pill-light: #e6e6e6;
    --fire-hot: #f6a21c;
    --fire-deep: #8a2e06;
  }
  * { box-sizing: border-box; margin: 0; padding: 0; }
  html, body { width: 902px; height: 1200px; overflow: hidden; background: var(--canvas); }
  body { position: relative; font-family: "Poppins", sans-serif; }

  .billboard {
    position: absolute; left: 21px; top: 385px;
    width: 860px; height: 430px;
    background: var(--board); overflow: hidden;
    box-shadow: 0 4px 14px rgba(0,0,0,.25);
  }
  .food-photo {
    position: absolute; left: 0; top: 0; width: 520px; height: 430px;
    background:
      radial-gradient(ellipse 120px 150px at 150px 170px, rgba(246,162,28,.85), rgba(138,46,6,.4) 60%, transparent 80%),
      radial-gradient(ellipse 150px 120px at 340px 200px, rgba(120,150,70,.7), rgba(150,70,30,.4) 55%, transparent 80%),
      radial-gradient(ellipse 220px 70px at 220px 290px, rgba(90,90,90,.8), transparent 75%),
      var(--board);
  }
  .direction-tab {
    position: absolute; left: 427px; top: 0; width: 237px; height: 75px;
    background: var(--white); border-radius: 0 0 36px 36px;
    display: flex; align-items: center; gap: 10px; padding-left: 36px;
  }
  .direction-icon { width: 45px; height: 45px; flex: none; }
  .direction-text { line-height: 1; }
  .direction-miles { color: var(--gold); font-weight: 700; font-size: 26px; }
  .direction-side { color: var(--ink); font-size: 15px; margin-top: 2px; padding-left: 8px; }

  .brand-name {
    position: absolute; left: 682px; top: 100px; width: 180px;
    text-align: center; color: var(--gold); font-weight: 500; font-size: 16px;
  }

  .headline { position: absolute; left: 433px; top: 130px; color: var(--white); }
  .headline-authentic { font-weight: 300; font-size: 62px; line-height: 1; letter-spacing: -1px; }
  .headline-thai { color: var(--gold); font-weight: 800; font-size: 83px; line-height: .9; letter-spacing: -1px; margin-left: 2px; }
  .headline-style {
    display: flex; align-items: center; gap: 8px; margin-top: 6px; margin-left: -2px;
    font-weight: 700; font-size: 46px; line-height: 1;
  }
  .headline-style .rule { width: 34px; height: 3px; background: var(--white); }
  .headline-style .script { font-family: "Great Vibes", cursive; font-weight: 400; font-size: 54px; margin-left: -2px; }

  .address-pill {
    position: absolute; left: 352px; top: 351px; width: 369px; height: 57px;
    background: var(--gold); border-radius: 0 29px 29px 0;
    display: flex; align-items: center; padding-left: 20px;
    color: var(--ink); font-weight: 700; font-size: 20px;
  }
  .phone-pill {
    position: absolute; left: 0; top: 334px; width: 358px; height: 96px;
    background: var(--pill-light); border-radius: 0 48px 0 0;
    display: flex; align-items: center; gap: 14px; padding-left: 20px;
    color: var(--ink); font-weight: 700; font-size: 35px; letter-spacing: .5px;
  }
  .phone-icon { width: 32px; height: 32px; flex: none; }
</style>
</head>
<body>
  <main class="billboard">
    <div class="food-photo" role="img" aria-label="Flaming wok with shrimp, broccoli and vegetables tossed in the air amid sparks"></div>

    <div class="direction-tab">
      <svg class="direction-icon" viewBox="0 0 45 45" aria-hidden="true">
        <circle cx="22.5" cy="22.5" r="21" fill="#1c1c1c" stroke="#d9a522" stroke-width="2.5"/>
        <path d="M13 13 L34 22.5 L13 32 L18 22.5 Z" fill="#d9a522"/>
      </svg>
      <div class="direction-text">
        <div class="direction-miles">6.5 Miles</div>
        <div class="direction-side">On The Right</div>
      </div>
    </div>

    <div class="brand-name">Lotus Leaf Kitchen</div>

    <div class="headline">
      <div class="headline-authentic">Authentic</div>
      <div class="headline-thai">Thai Food</div>
      <div class="headline-style">
        <span class="rule"></span>
        <span>Bangkok</span>
        <span class="script">Style</span>
        <span class="rule"></span>
      </div>
    </div>

    <div class="address-pill">4126 Maple Ridge Rd Otto NC</div>

    <div class="phone-pill">
      <svg class="phone-icon" viewBox="0 0 32 32" aria-hidden="true">
        <path d="M7 4 L12 4 L14 10 L11 12 C12.5 16 15.5 19.5 20 21 L22 18 L28 20 L28 25 C28 27 26.5 28 24.5 28 C14 27 5 18 4 7.5 C4 5.5 5 4 7 4 Z" fill="#1c1c1c"/>
        <path d="M19 6 A7 7 0 0 1 26 13 M19 2 A11 11 0 0 1 30 13" fill="none" stroke="#1c1c1c" stroke-width="2" stroke-linecap="round"/>
      </svg>
      <span>828-555-4172</span>
    </div>
  </main>
</body>
</html>
```